Velvet Lagoon Charm Boutique

Looking to refresh our old business cards. We are a girls/tween birthday party store and salon specializing in princess, glamour and spa parties. I would like to maintain the same colors (hot pink and turquoise). Would like the card to be feminine, fun and glitzy..

Target Market(s)

Parents of girls and girls aged 4-14

Industry/Entity Type

Store

Font styles to use
Script

Colors
e34197
85cae6

Requirements
Must have
• name phone and address
colors of hot pink and turquoise
appointment day and time field on one side
Nice to have
• creativity
Should not have
• picture of lipstick

```html
<!DOCTYPE html>
<html lang="en">
<head>
<meta charset="utf-8">
<title>Velvet Lagoon Charm Boutique — Business Card</title>
<link rel="stylesheet" href="https://fonts.googleapis.com/css2?family=Quicksand:wght@400;500&family=Dancing+Script:wght@500;700&display=swap">
<style>
  :root {
    --hot-pink: #e34197;
    --pink-deep: #e8388f;
    --turquoise: #1bb8d8;
    --turquoise-soft: #85cae6;
    --card-white: #ffffff;
    --blush: #fbe3ef;
    --backdrop: #3b3b3d;
  }
  * { margin: 0; padding: 0; box-sizing: border-box; }
  html, body { width: 1200px; height: 1000px; overflow: hidden; }
  body {
    background: var(--backdrop);
    font-family: "Quicksand", sans-serif;
    position: relative;
  }
  .card {
    position: absolute;
    width: 660px;
    height: 378px;
    background: var(--card-white);
    overflow: hidden;
    box-shadow: 0 10px 30px rgba(0,0,0,.45);
  }
  .card--front { left: 60px; top: 90px; }
  .card--back { left: 480px; top: 530px; }

  .front-wave { position: absolute; inset: 0; width: 100%; height: 100%; }

  .holder {
    position: absolute;
    top: 24px;
    right: 40px;
    text-align: right;
  }
  .holder__name { color: var(--hot-pink); font-size: 27px; font-weight: 400; line-height: 1.1; }
  .holder__role { color: var(--turquoise); font-size: 19px; font-weight: 400; line-height: 1.2; }

  .contact {
    position: absolute;
    right: 40px;
    bottom: 44px;
    text-align: right;
    color: var(--card-white);
    font-size: 17px;
    line-height: 1.55;
    font-style: normal;
  }
  .contact__phone { color: var(--turquoise-soft); margin-bottom: 10px; }
  .contact__phone svg { width: 14px; height: 14px; vertical-align: -2px; margin-right: 6px; }
  .contact__shop { color: var(--turquoise-soft); }

  .brand {
    position: absolute;
    left: 40px;
    top: 150px;
    width: 230px;
    display: flex;
    align-items: center;
    gap: 12px;
  }
  .brand__dot {
    flex: none;
    width: 16px; height: 16px;
    border-radius: 50%;
    background: var(--turquoise);
  }
  .brand__name {
    color: var(--hot-pink);
    font-size: 25px;
    font-weight: 500;
    line-height: 1.2;
  }

  .appointment-frame {
    position: absolute;
    left: 40px; top: 30px;
    width: 580px; height: 318px;
    border-radius: 90px / 70px;
    background: radial-gradient(ellipse at center, var(--card-white) 55%, var(--blush) 100%);
    border: 3px solid var(--hot-pink);
  }
  .appointment__title {
    position: absolute;
    top: 62px; left: 0; right: 0;
    text-align: center;
    font-family: "Dancing Script", cursive;
    font-weight: 700;
    font-size: 40px;
    color: var(--hot-pink);
  }
  .appointment__fields {
    position: absolute;
    left: 130px; right: 130px; top: 140px;
    list-style: none;
  }
  .appointment__field {
    display: flex;
    align-items: flex-end;
    gap: 12px;
    height: 50px;
    font-family: "Dancing Script", cursive;
    font-weight: 500;
    font-size: 26px;
    color: var(--turquoise);
  }
  .appointment__field span { width: 62px; }
  .appointment__line {
    flex: 1;
    border-bottom: 2px solid var(--turquoise);
    margin-bottom: 8px;
  }
</style>
</head>
<body>

<section class="card card--front" aria-label="Business card front">
  <svg class="front-wave" viewBox="0 0 660 378" preserveAspectRatio="none" aria-hidden="true">
    <path d="M700 108 C520 112 370 128 345 210 C325 280 280 340 200 378 L700 378 Z" fill="var(--pink-deep)"/>
    <path d="M700 108 C520 112 370 128 345 210 C325 280 280 340 200 378" transform="translate(-10 -7)" fill="none" stroke="var(--turquoise)" stroke-width="9"/>
    <path d="M700 108 C520 112 370 128 345 210 C325 280 280 340 200 378" transform="translate(-23 -16)" fill="none" stroke="var(--turquoise-soft)" stroke-width="7"/>
  </svg>

  <div class="brand">
    <span class="brand__dot" aria-hidden="true"></span>
    <span class="brand__name">Velvet Lagoon Charm Boutique</span>
  </div>

  <div class="holder">
    <p class="holder__name">Rosalie Hartwell</p>
    <p class="holder__role">Beauty Therapist</p>
  </div>

  <address class="contact">
    <p class="contact__phone">
      <svg viewBox="0 0 24 24" aria-hidden="true"><path fill="currentColor" d="M6.6 10.8a15.1 15.1 0 0 0 6.6 6.6l2.2-2.2a1 1 0 0 1 1-.25 11.4 11.4 0 0 0 3.6.57 1 1 0 0 1 1 1V20a1 1 0 0 1-1 1A17 17 0 0 1 3 4a1 1 0 0 1 1-1h3.5a1 1 0 0 1 1 1c0 1.25.2 2.45.57 3.57a1 1 0 0 1-.25 1z"/></svg>Phone: 555 (214) 0187
    </p>
    <p class="contact__shop">Velvet Lagoon Charm Boutique</p>
    <p>48 Willow Bend Lane</p>
    <p>Fairhaven, Ohio 44021</p>
  </address>
</section>

<section class="card card--back" aria-label="Business card back">
  <div class="appointment-frame" role="img" aria-label="Decorative pink scrolled frame with confetti flourishes"></div>
  <h2 class="appointment__title">Appointment</h2>
  <ul class="appointment__fields">
    <li class="appointment__field"><span>Name:</span><i class="appointment__line"></i></li>
    <li class="appointment__field"><span>Date:</span><i class="appointment__line"></i></li>
    <li class="appointment__field"><span>Time:</span><i class="appointment__line"></i></li>
  </ul>
</section>

</body>
</html>
```